Bluefern painting and decorating *

Need a flyer design to advertise my services
So the information I need included is the services we offer at bluefern painting and decorating which include
Interior painting
Exterior painting
Wallpaper hanging
Paint and cellulose spraying
Dust free sanding
Pressure washing
Stone cleaning
Also would need to have my company contact details in
Www.bluefernpaintingdecorating.co.uk
Email is info@bluefernpaintingdecorating.com
Bluefern Painting & Decorating Services has a proven track record of innovative designs, effective problem solving and attention to detail and our goal is to meet and exceed the expectations of every customer. We take on all types of jobs from small domestic work to larger commercial projects, all carried out to the highest standards, and at very competitive prices.

```html
<!DOCTYPE html>
<html lang="en">
<head>
<meta charset="utf-8">
<title>Bluefern Painting and Decorating – Flyer</title>
<link rel="stylesheet" href="https://fonts.googleapis.com/css2?family=Bebas+Neue&family=Montserrat:wght@600;700&family=Open+Sans:wght@600;700&family=Roboto+Condensed:wght@700&display=swap">
<style>
  :root {
    --navy: #0b4176;
    --panel: #0d4a82;
    --accent: #4a9be0;
    --sky: #9fd0f4;
    --ink: #1b1b1b;
    --paper: #ffffff;
    --bar: #3a3a3a;
    --page: #e6e6e6;
  }
  html, body { margin: 0; padding: 0; overflow: hidden; background: var(--page); }
  .flyer {
    position: relative; width: 852px; height: 1200px; overflow: hidden;
    background: var(--paper); font-family: "Open Sans", sans-serif;
  }
  .abs { position: absolute; }

  /* brand block */
  .brand { left: 42px; top: 48px; width: 340px; text-align: center; color: var(--navy); font-family: "Open Sans", sans-serif; font-weight: 700; }
  .brand-name { font-size: 54px; line-height: 1; letter-spacing: 1px; text-transform: uppercase; }
  .brand-tag { font-size: 15.5px; letter-spacing: .3px; text-transform: uppercase; margin-top: 4px; }
  .brand-rule { left: 50px; top: 152px; width: 322px; height: 2px; background: var(--navy); }

  .headline { left: 36px; top: 218px; width: 358px; text-align: center; }
  .headline-name { font-family: "Bebas Neue", sans-serif; font-size: 116px; line-height: .92; color: var(--navy); }
  .headline-sub { font-family: "Roboto Condensed", sans-serif; font-weight: 700; font-size: 25px; color: var(--accent); letter-spacing: .5px; text-transform: uppercase; margin-top: 6px; }

  .gallery-photo {
    left: 36px; width: 350px; height: 218px; box-sizing: border-box;
    border: 3px solid var(--navy); border-radius: 12px;
  }
  .photo-living { top: 413px; background: linear-gradient(180deg, #f1ece3 0%, #e7ddcf 55%, #c9a27a 80%, #efe9e0 100%); }
  .photo-wall { top: 673px; background: linear-gradient(180deg, #f3f3f3 0%, #e9e9e9 60%, #d7c9b0 85%, #f5f5f5 100%); }

  /* right column */
  .interior-photo {
    left: 425px; top: 0; width: 427px; height: 360px;
    background: linear-gradient(180deg, #dfe4ea 0%, #c9d2dc 45%, #6f8fb3 75%, var(--panel) 100%);
  }
  .offer-panel { left: 425px; top: 355px; width: 427px; height: 525px; background: var(--panel); }
  .offer-title { left: 472px; top: 337px; font-family: "Montserrat", sans-serif; font-weight: 700; font-size: 37px; color: #fff; letter-spacing: .5px; }
  .offer-title span { color: var(--accent); }
  .offer-rule { left: 472px; top: 398px; width: 64px; height: 3px; background: #fff; }
  .offer-list { left: 472px; top: 436px; margin: 0; padding: 0; list-style: none; }
  .offer-list li { display: flex; align-items: center; height: 51.6px; font-family: "Montserrat", sans-serif; font-weight: 600; font-size: 21px; color: #fff; }
  .offer-list svg { width: 17px; height: 17px; margin-right: 21px; flex: none; }

  .painter-photo {
    left: 560px; top: 808px; width: 292px; height: 392px;
    background: linear-gradient(180deg, #f4f6f8 0%, #e9eef4 20%, #2b5fc2 45%, #1f4fae 70%, #f2f2f2 90%, #ffffff 100%);
  }

  /* contact */
  .phone-band { left: 0; top: 968px; }
  .phone-number { left: 128px; top: 974px; font-family: "Roboto Condensed", sans-serif; font-weight: 700; font-size: 42px; line-height: 44px; color: #fff; letter-spacing: .5px; }
  .contact-line { left: 50px; display: flex; align-items: center; font-family: "Roboto Condensed", sans-serif; font-weight: 700; font-size: 16px; color: var(--ink); }
  .contact-line svg { width: 22px; height: 18px; margin-right: 18px; }
  .contact-email { top: 1047px; }
  .contact-web { top: 1076px; }
  .follow { left: 42px; top: 1130px; display: flex; align-items: center; }
  .follow-label { font-family: "Roboto Condensed", sans-serif; font-weight: 700; font-size: 21px; color: var(--accent); text-decoration: underline; margin-right: 10px; }
  .social-dot { width: 25px; height: 25px; border-radius: 50%; background: var(--accent); margin-right: 13px; }
  .footer-bar { left: 0; top: 1181px; width: 584px; height: 19px; background: var(--bar); }
</style>
</head>
<body>
<div class="flyer">

  <div class="abs brand">
    <div class="brand-name">Bluefern</div>
    <div class="brand-tag">Painting and decorating services</div>
  </div>
  <div class="abs brand-rule"></div>

  <div class="abs headline">
    <div class="headline-name">BLUEFERN</div>
    <div class="headline-sub">Painting and decorating</div>
  </div>

  <div class="abs gallery-photo photo-living" role="img" aria-label="Freshly painted living and dining room with orange wall art"></div>
  <div class="abs gallery-photo photo-wall" role="img" aria-label="White painted brick wall with hanging plants above a table"></div>

  <div class="abs interior-photo" role="img" aria-label="Bright modern open-plan kitchen and dining interior"></div>
  <div class="abs offer-panel"></div>

  <div class="abs offer-title">WE <span>OFFER</span></div>
  <div class="abs offer-rule"></div>
  <ul class="abs offer-list">
    <li><svg viewBox="0 0 20 20"><circle cx="10" cy="10" r="10" fill="#8fc3ee"/><path d="M5.5 10.3l3 3 6-6.3" fill="none" stroke="#0d4a82" stroke-width="2.4" stroke-linecap="round" stroke-linejoin="round"/></svg>Interior painting</li>
    <li><svg viewBox="0 0 20 20"><circle cx="10" cy="10" r="10" fill="#8fc3ee"/><path d="M5.5 10.3l3 3 6-6.3" fill="none" stroke="#0d4a82" stroke-width="2.4" stroke-linecap="round" stroke-linejoin="round"/></svg>Exterior painting</li>
    <li><svg viewBox="0 0 20 20"><circle cx="10" cy="10" r="10" fill="#8fc3ee"/><path d="M5.5 10.3l3 3 6-6.3" fill="none" stroke="#0d4a82" stroke-width="2.4" stroke-linecap="round" stroke-linejoin="round"/></svg>Wallpaper hanging</li>
    <li><svg viewBox="0 0 20 20"><circle cx="10" cy="10" r="10" fill="#8fc3ee"/><path d="M5.5 10.3l3 3 6-6.3" fill="none" stroke="#0d4a82" stroke-width="2.4" stroke-linecap="round" stroke-linejoin="round"/></svg>Paint &amp; cellulose spraying</li>
    <li><svg viewBox="0 0 20 20"><circle cx="10" cy="10" r="10" fill="#8fc3ee"/><path d="M5.5 10.3l3 3 6-6.3" fill="none" stroke="#0d4a82" stroke-width="2.4" stroke-linecap="round" stroke-linejoin="round"/></svg>Dust free sanding</li>
    <li><svg viewBox="0 0 20 20"><circle cx="10" cy="10" r="10" fill="#8fc3ee"/><path d="M5.5 10.3l3 3 6-6.3" fill="none" stroke="#0d4a82" stroke-width="2.4" stroke-linecap="round" stroke-linejoin="round"/></svg>Pressure washing</li>
    <li><svg viewBox="0 0 20 20"><circle cx="10" cy="10" r="10" fill="#8fc3ee"/><path d="M5.5 10.3l3 3 6-6.3" fill="none" stroke="#0d4a82" stroke-width="2.4" stroke-linecap="round" stroke-linejoin="round"/></svg>Stone cleaning</li>
  </ul>

  <div class="abs painter-photo" role="img" aria-label="Decorator in blue shirt and white overalls rolling blue paint onto a wall, seen from behind"></div>

  <svg class="abs phone-band" width="460" height="58" viewBox="0 0 460 58" aria-hidden="true">
    <rect x="36" y="6" width="414" height="46" rx="4" fill="var(--sky)"/>
    <rect x="36" y="6" width="14" height="46" fill="var(--accent)"/>
    <circle cx="90" cy="29" r="18" fill="var(--navy)"/>
    <circle cx="90" cy="29" r="13" fill="none" stroke="#fff" stroke-width="2"/>
    <path d="M84 22c1-1 2-1 3 0l2 3c.5 1 0 2-.8 2.5-.5.4-.5 1 0 1.8l1.5 1.8c.6.6 1.2.8 1.8.2.7-.8 1.7-1 2.5-.3l2.5 2c.8.8.6 1.8-.3 2.6-2 1.8-5 1-8-2-3.5-3.5-4.8-7-3.2-9.6z" fill="#fff"/>
  </svg>
  <div class="abs phone-number">07700 900 415</div>

  <div class="abs contact-line contact-email">
    <svg viewBox="0 0 22 18"><rect x="1" y="2" width="20" height="14" rx="1.5" fill="var(--accent)"/><path d="M2 3.5l9 7 9-7" fill="none" stroke="#fff" stroke-width="1.6"/></svg>
    info@bluefernpaintingdecorating.com
  </div>
  <div class="abs contact-line contact-web">
    <svg viewBox="0 0 22 18"><circle cx="11" cy="9" r="8" fill="none" stroke="var(--accent)" stroke-width="2"/><ellipse cx="11" cy="9" rx="3.5" ry="8" fill="none" stroke="var(--accent)" stroke-width="1.5"/><path d="M3 9h16M4.5 5h13M4.5 13h13" stroke="var(--accent)" stroke-width="1.3"/></svg>
    www.bluefernpaintingdecorating.co.uk
  </div>

  <div class="abs follow">
    <span class="follow-label">Follow US :</span>
    <span class="social-dot"></span>
    <span class="social-dot"></span>
    <span class="social-dot"></span>
    <span class="social-dot"></span>
    <svg width="28" height="20" viewBox="0 0 28 20" aria-hidden="true"><rect x="1" y="2" width="26" height="16" rx="2" fill="var(--accent)"/><path d="M2 3.5l12 8 12-8" fill="none" stroke="#fff" stroke-width="1.8"/></svg>
  </div>

  <div class="abs footer-bar"></div>
</div>
</body>
</html>
```